依頼詳細
展示会の会場を歩いているお客様に一目でこの商品がどのようなものかを理解していただけるような、わかりやすく、目を引くインパクトのあるデザインを希望します。
記載項目
商品名(点検口の安全金網 Rフレア)/社名/キャッチコピー/ロゴ
詳細は添付ファイル参照
サイズ
B1(縦横どちらも可)
ページ数
片面
希望イメージ
シンプル 複雑
単色 カラフル
暗い 明るい
日常 高級
遊び心 厳粛
未来的 伝統的
女性的 男性的
希望する色
オレンジ(黄色めの)と黒 その他の色も可
納品ファイル
• 高解像度JPG (.jpg)
• イラストレーター形式 (.ai)
補足説明
Rフレア http://item.sorabazaar.jp/lumo-shop/c/0000000830/
点検口 http://item.sorabazaar.jp/lumo-shop/c/0000000480/

```html
<!DOCTYPE html>
<html lang="ja">
<head>
<meta charset="utf-8">
<title>点検口の安全金網 Rフレア</title>
<link href="https://fonts.googleapis.com/css2?family=Noto+Sans+JP:wght@700;900&display=swap" rel="stylesheet">
<style>
:root{
  --yellow:#ffe600;
  --red:#e8231a;
  --black:#111;
  --white:#fff;
  --photo-main:#d9553a;
}
*{margin:0;padding:0;box-sizing:border-box}
html,body{width:849px;height:1200px;overflow:hidden}
body{background:var(--yellow);font-family:"Noto Sans JP",sans-serif;color:var(--black)}
.poster{position:relative;width:849px;height:1200px;background:var(--yellow);overflow:hidden}
.product-photo{position:absolute;left:28px;top:20px;width:560px;height:570px;
  background:radial-gradient(ellipse at 45% 55%, #f0c23a 0 22%, var(--photo-main) 42%, #b8432c 62%, var(--yellow) 74%)}
.headline{position:absolute;writing-mode:vertical-rl;white-space:nowrap;font-weight:900;line-height:1}
.headline .em{color:var(--red);-webkit-text-stroke:8px var(--white);paint-order:stroke fill}
.headline-first{right:58px;top:34px;font-size:68px}
.headline-second{right:190px;top:110px;font-size:63px}
.features{position:absolute;left:42px;top:488px;list-style:none;font-weight:900;font-size:38px;line-height:1.5}
.features li{display:flex;align-items:center;gap:10px;white-space:nowrap}
.features svg{width:38px;height:38px;flex:none}
.band{position:absolute;left:0;top:800px;width:849px;height:50px;background:var(--black);
  color:var(--white);font-weight:900;font-size:26px;display:flex;align-items:center;justify-content:center;letter-spacing:1px;white-space:nowrap}
.thumb-card{position:absolute;left:42px;top:882px;width:326px;height:250px;background:var(--white);border-radius:18px}
.thumb-card::after{content:"";position:absolute;right:-22px;top:80px;border-left:24px solid var(--white);
  border-top:14px solid transparent;border-bottom:14px solid transparent}
.thumb-photo{position:absolute;left:28px;top:24px;width:270px;height:180px;border-radius:6px;
  background:linear-gradient(160deg,#f2f2f2,#b7b7b7)}
.thumb-label{position:absolute;left:30px;bottom:14px;font-size:11px;font-weight:700}
.product-kind{position:absolute;left:398px;top:918px;font-weight:900;font-size:30px;line-height:1.3;white-space:nowrap}
.product-name{position:absolute;left:578px;top:914px;font-weight:900;font-size:62px;line-height:1;white-space:nowrap}
.company{position:absolute;right:46px;top:1012px;font-weight:900;font-size:25px;white-space:nowrap}
</style>
</head>
<body>
<main class="poster">
  <div class="product-photo" role="img" aria-label="安全金網を取り付けたオレンジ色の点検口の製品写真"></div>

  <h1>
    <span class="headline headline-first">「<span class="em">工具の落下</span>」や</span>
    <span class="headline headline-second">「<span class="em">手足の侵入</span>」を防止。</span>
  </h1>

  <ul class="features">
    <li><svg viewBox="0 0 40 40"><rect x="3" y="8" width="28" height="28" fill="#fff" stroke="#111" stroke-width="2"/><path d="M9 21l8 8L37 5" fill="none" stroke="#e8231a" stroke-width="6" stroke-linecap="round"/></svg>溶接不要</li>
    <li><svg viewBox="0 0 40 40"><rect x="3" y="8" width="28" height="28" fill="#fff" stroke="#111" stroke-width="2"/><path d="M9 21l8 8L37 5" fill="none" stroke="#e8231a" stroke-width="6" stroke-linecap="round"/></svg>3分で取付け取外し</li>
    <li><svg viewBox="0 0 40 40"><rect x="3" y="8" width="28" height="28" fill="#fff" stroke="#111" stroke-width="2"/><path d="M9 21l8 8L37 5" fill="none" stroke="#e8231a" stroke-width="6" stroke-linecap="round"/></svg>しかも、ローコスト</li>
  </ul>

  <div class="band">現場の作業者を機械の巻込まれ事故から守る！</div>

  <div class="thumb-card">
    <div class="thumb-photo" role="img" aria-label="安全金網単体の製品写真"></div>
    <span class="thumb-label">Rフレア</span>
  </div>

  <p class="product-kind">点検口の<br>安全金網</p>
  <p class="product-name">Rフレア</p>
  <p class="company">株式会社ミナトテクノ</p>
</main>
</body>
</html>
```